Family Values Statement Image

I have created a statement of values for my family. Our last name is Tolvimar, and we are using those letters as an acronym. I would like an image with these words and letters with a tree with deep roots, where the roots are the focal point.

A - All In
N - Never Settle
D - Dependable
E - Enthusiastic
R - Repair
E - Enduring
G - Gushy Hearted
G - Gratitudes

Note that "gratitudes" is intentionally misspelled.

• On further reflection, I am interested in the words being much more prominent than the tree. In fact, the tree could be quite small or even just a watermark behind the words.

```html
<!DOCTYPE html>
<html lang="en">
<head>
<meta charset="utf-8">
<title>Tolvimar Family Values</title>
<link rel="stylesheet" href="https://fonts.googleapis.com/css2?family=Tinos:ital,wght@1,700&display=swap">
<style>
  :root {
    --page: #ffffff;
    --poster: #133441;
    --panel: #1c4b58;
    --panel-deep: #163e4a;
    --gold: #c7a76a;
    --leaf: #5e7d45;
    --ink: #1a1a1a;
    --text: #ffffff;
  }
  * { margin: 0; padding: 0; box-sizing: border-box; }
  html, body { width: 848px; height: 1200px; overflow: hidden; background: var(--page); }
  .canvas { position: relative; width: 848px; height: 1200px; }
  .poster {
    position: absolute; left: 106px; top: 149px; width: 636px; height: 900px;
    background: var(--poster);
  }
  .frame {
    position: absolute; left: 22px; top: 20px; width: 595px; height: 862px;
    border: 1.5px solid var(--gold);
    background: radial-gradient(ellipse at 55% 45%, var(--panel) 0%, var(--panel-deep) 100%);
    overflow: hidden;
  }
  .tree-art {
    position: absolute; left: 2px; top: 25px; width: 483px; height: 810px;
    background:
      radial-gradient(ellipse 48% 30% at 50% 28%, rgba(110,140,80,0.55), rgba(110,140,80,0) 100%),
      radial-gradient(ellipse 12% 30% at 52% 60%, rgba(199,167,106,0.55), rgba(199,167,106,0) 100%),
      radial-gradient(ellipse 45% 20% at 50% 82%, rgba(199,167,106,0.40), rgba(199,167,106,0) 100%);
  }
  .values {
    position: absolute; left: 162px; top: 172px; list-style: none;
    font-family: "Tinos", "Times New Roman", serif; font-style: italic; font-weight: 700;
  }
  .value {
    height: 62px; display: flex; align-items: baseline; white-space: nowrap;
  }
  .initial {
    font-size: 70px; color: var(--leaf); line-height: 1;
    -webkit-text-stroke: 3px var(--ink); paint-order: stroke fill;
    width: 54px; display: inline-block;
  }
  .word {
    font-size: 50px; color: var(--text); line-height: 1;
    -webkit-text-stroke: 5px var(--ink); paint-order: stroke fill;
    letter-spacing: -0.5px;
  }
</style>
</head>
<body>
<div class="canvas">
  <section class="poster">
    <div class="frame">
      <div class="tree-art" role="img" aria-label="Illustrated tree of life with green and gold leaves and deep roots knotted into a Celtic heart"></div>
      <ul class="values">
        <li class="value"><span class="initial">T</span><span class="word">eam First</span></li>
        <li class="value"><span class="initial">O</span><span class="word">nward Ever</span></li>
        <li class="value"><span class="initial">L</span><span class="word">oyal Always</span></li>
        <li class="value"><span class="initial">V</span><span class="word">ivacious</span></li>
        <li class="value"><span class="initial">I</span><span class="word">mprove</span></li>
        <li class="value"><span class="initial">M</span><span class="word">ade to Last</span></li>
        <li class="value"><span class="initial">A</span><span class="word">ffectionate</span></li>
        <li class="value"><span class="initial">R</span><span class="word">ich in Thanks</span></li>
      </ul>
    </div>
  </section>
</div>
</body>
</html>
```